We need a corporate presentation for our software factory.

We need to make a detailed brochure for a presentation of our company and our software products and solutions. We are a software house capable of carrying out any project. We need a design like our web-site www.lintaro.it, that reflects our logos. In particular, the VEXO.TRIM product should be highlighted.

```html
<!DOCTYPE html>
<html lang="en">
<head>
<meta charset="utf-8">
<title>Lintaro Software Factory – Brochure</title>
<link rel="stylesheet" href="https://fonts.googleapis.com/css2?family=Montserrat:wght@300;400;600;700;800&family=Open+Sans:wght@400;600;700&display=swap">
<style>
:root{
  --teal:#17aebd;
  --teal-dark:#0f98a6;
  --ink:#333a3f;
  --grey:#6d7378;
  --paper:#f5f5f4;
  --paper-2:#e9eaea;
  --stage:#dcdde0;
  --night:#10365a;
  --night-2:#2a79a8;
}
*{box-sizing:border-box;margin:0;padding:0}
html,body{width:1200px;height:2387px;overflow:hidden;background:var(--stage)}
body{position:relative;font-family:"Open Sans",Arial,sans-serif;color:var(--ink)}
.spread{position:absolute;left:80px;width:1040px;height:735px;display:flex;box-shadow:0 14px 40px rgba(0,0,0,.18)}
.spread--cover{top:45px}
.spread--profile{top:825px}
.spread--solutions{top:1605px}
.page{position:relative;width:520px;height:735px;overflow:hidden;background:var(--paper)}
.page + .page{border-left:1px solid rgba(0,0,0,.06)}
.abs{position:absolute}
svg.abs{left:0;top:0}

/* brand name */
.brand{position:absolute;display:flex;align-items:center;gap:8px;font-family:"Montserrat",sans-serif;font-weight:300;font-size:30px;color:var(--grey);letter-spacing:.5px}
.brand__dot{width:16px;height:16px;border-radius:50%;background:var(--teal)}
.brand--light{color:#fff}
.brand--light .brand__dot{background:#fff}
.brand--small{font-size:24px}
.brand--small .brand__dot{width:13px;height:13px}

/* cover */
.back-cover{background:var(--teal)}
.back-cover__contact{position:absolute;left:40px;top:470px}
.contact-title{font-family:"Montserrat",sans-serif;font-weight:700;font-size:17px;color:var(--teal);letter-spacing:.5px;border-bottom:2px solid var(--teal);display:inline-block;margin:14px 0 14px}
.contact-list{list-style:none;font-family:"Montserrat",sans-serif;font-weight:600;font-size:13px;color:var(--ink)}
.contact-list li{display:flex;align-items:center;gap:10px;margin-bottom:7px}
.contact-list svg{width:12px;height:12px;fill:var(--teal)}
.front-cover__title{position:absolute;left:60px;top:505px}
.cover-name{font-family:"Montserrat",sans-serif;font-weight:800;font-size:64px;line-height:1;color:var(--teal);letter-spacing:2px}
.cover-sub{font-family:"Montserrat",sans-serif;font-weight:400;font-size:31px;color:var(--grey);letter-spacing:3px;margin-top:2px}
.cover-rule{width:110px;height:1px;background:var(--grey);margin:14px 0 10px}
.cover-url{font-family:"Montserrat",sans-serif;font-weight:600;font-size:17px;color:var(--teal);letter-spacing:4px}

/* inner pages */
.heading{font-family:"Montserrat",sans-serif;font-weight:700;color:var(--teal);letter-spacing:.5px}
.heading--xl{font-size:24px}
.heading--md{font-size:15px}
.heading--sm{font-size:11px;margin:10px 0 3px}
.copy{font-size:8.6px;line-height:1.55;color:var(--ink)}
.copy p{margin-bottom:6px}
.copy--white{color:#fff}
.copy--white .heading{color:#fff}
.url-tab{position:absolute;right:22px;bottom:22px;display:flex;align-items:center}
.url-tab__label{background:var(--teal);color:#fff;font-family:"Montserrat",sans-serif;font-weight:700;font-size:12px;letter-spacing:1.5px;padding:5px 26px 5px 18px;border-radius:12px 0 0 12px}
.url-tab__num{width:28px;height:28px;border-radius:50%;background:#222;color:#fff;font-family:"Montserrat",sans-serif;font-size:11px;font-weight:600;display:flex;align-items:center;justify-content:center;margin-left:-10px;border:2px solid #fff}
.footer-rule{position:absolute;height:1px;background:var(--grey)}
.band-label{position:absolute;font-family:"Montserrat",sans-serif;font-weight:800;font-size:22px;color:#fff;letter-spacing:1px}
.band-label small{display:block;font-size:7px;font-weight:600;letter-spacing:2.5px;margin-top:2px}
.columns{position:absolute;left:40px;top:330px;width:440px;display:flex;gap:26px}
.columns .col{flex:1}
.columns .divider{width:0;border-left:2px dotted var(--grey)}
.bullets{list-style:none;font-size:8.6px;line-height:1.5}
.bullets li{position:relative;padding-left:16px;margin-bottom:4px}
.bullets li::before{content:"";position:absolute;left:0;top:3px;width:8px;height:8px;border-radius:50%;background:var(--teal)}
.label-tab{position:absolute;background:var(--teal);color:#fff;font-family:"Montserrat",sans-serif;font-weight:700;font-size:12px;letter-spacing:1px;padding:5px 22px;border-radius:4px}
.tech-box{position:absolute;left:40px;top:370px;width:445px;height:250px;background:var(--paper-2);padding:16px 18px}
.tech-grid{display:grid;grid-template-columns:repeat(10,1fr);gap:8px;margin-top:10px}
.tech-grid span{height:30px;border-radius:5px}
</style>
</head>
<body>

<!-- ===== Cover spread ===== -->
<section class="spread spread--cover">
  <article class="page back-cover">
    <svg class="abs" width="520" height="735" viewBox="0 0 520 735">
      <circle cx="270" cy="220" r="150" fill="rgba(0,0,0,.07)"/>
      <circle cx="40" cy="610" r="255" fill="var(--paper)"/>
    </svg>
    <div class="back-cover__contact">
      <div class="brand" style="position:static"><span class="brand__dot"></span>lintaro</div>
      <div class="contact-title">CONTACT US</div>
      <ul class="contact-list">
        <li><svg viewBox="0 0 24 24"><path d="M6.6 10.8a15 15 0 0 0 6.6 6.6l2.2-2.2c.3-.3.7-.4 1-.2 1.1.4 2.3.6 3.6.6.6 0 1 .4 1 1V20c0 .6-.4 1-1 1A17 17 0 0 1 3 4c0-.6.4-1 1-1h3.5c.6 0 1 .4 1 1 0 1.3.2 2.5.6 3.6.1.3 0 .7-.2 1z"/></svg>+39 049.5510720</li>
        <li><svg viewBox="0 0 24 24"><rect x="3" y="8" width="18" height="10" rx="2"/><rect x="7" y="3" width="10" height="6"/></svg>+39 049.5510731</li>
        <li><svg viewBox="0 0 24 24"><rect x="2" y="5" width="20" height="14" rx="2"/></svg>info@lintaro.it</li>
        <li><svg viewBox="0 0 24 24"><circle cx="12" cy="12" r="10"/></svg>www.lintaro.it</li>
      </ul>
    </div>
  </article>

  <article class="page front-cover">
    <svg class="abs" width="520" height="735" viewBox="0 0 520 735">
      <circle cx="490" cy="150" r="68" fill="none" stroke="var(--teal)" stroke-width="1"/>
      <circle cx="470" cy="710" r="62" fill="none" stroke="var(--teal)" stroke-width="1"/>
      <circle cx="265" cy="320" r="168" fill="none" stroke="var(--teal)" stroke-width="2"/>
      <circle cx="265" cy="320" r="156" fill="var(--teal)"/>
      <defs>
        <radialGradient id="cloudGrad" cx="50%" cy="45%" r="60%">
          <stop offset="0" stop-color="var(--night-2)"/>
          <stop offset="1" stop-color="var(--night)"/>
        </radialGradient>
      </defs>
      <circle cx="265" cy="320" r="146" fill="url(#cloudGrad)" role="img" aria-label="Word cloud of software development terms"/>
    </svg>
    <div class="brand" style="left:60px;top:62px"><span class="brand__dot"></span>lintaro</div>
    <div class="front-cover__title">
      <div class="cover-name">LINTARO</div>
      <div class="cover-sub">SOFTWARE FACTORY</div>
      <div class="cover-rule"></div>
      <div class="cover-url">www.lintaro.it</div>
    </div>
  </article>
</section>

<!-- ===== Profile & products spread ===== -->
<section class="spread spread--profile">
  <article class="page">
    <svg class="abs" width="520" height="735" viewBox="0 0 520 735">
      <path d="M0 430 C170 450 330 520 400 640 L440 735 L0 735 Z" fill="var(--teal)"/>
      <path d="M0 470 C170 490 300 560 360 660" fill="none" stroke="var(--teal-dark)" stroke-width="1"/>
      <circle cx="195" cy="560" r="112" fill="none" stroke="#fff" stroke-width="3"/>
      <circle cx="195" cy="560" r="102" fill="#fff"/>
      <defs>
        <linearGradient id="techGrad" x1="0" y1="0" x2="1" y2="1">
          <stop offset="0" stop-color="#1b2c4a"/>
          <stop offset=".55" stop-color="#3a6fa8"/>
          <stop offset="1" stop-color="#8fb3d8"/>
        </linearGradient>
      </defs>
      <circle cx="195" cy="560" r="92" fill="url(#techGrad)" role="img" aria-label="Software concept image with digital interface"/>
    </svg>
    <div class="abs copy" style="left:40px;top:40px;width:440px">
      <h2 class="heading heading--xl" style="margin-bottom:12px">COMPANY PROFILE</h2>
      <p>Lintaro was founded in 2005 with the aim of producing specialised software built with modern technologies and clear methods, following every client from the first idea to final delivery and support.</p>
      <p>The company works with public bodies and private firms, designing platforms that manage data, people and processes across many sectors, with particular care for usability and security.</p>
      <p><b>Lintaro has grown through long partnerships</b> with research groups and universities, turning new ideas into stable products used every day by thousands of users.</p>
      <p>Over the years the team has built systems for large events, health services and industry, always aiming at reliable results and a high quality of service.</p>
      <p>Today Lintaro offers both ready products and custom projects, with a team able to handle analysis, design, development and hosting in house.</p>
      <p>From its beginnings to the present, the company has kept a simple goal: useful software that lasts.</p>
    </div>
    <div class="brand brand--light brand--small" style="left:26px;top:655px"><span class="brand__dot"></span>lintaro</div>
    <div class="url-tab"><span class="url-tab__label">www.lintaro.it</span><span class="url-tab__num">01</span></div>
  </article>

  <article class="page">
    <svg class="abs" width="520" height="735" viewBox="0 0 520 735">
      <path d="M0 40 L330 40 L300 120 L0 120 Z" fill="var(--teal)"/>
      <circle cx="405" cy="120" r="112" fill="#fff"/>
      <circle cx="405" cy="120" r="104" fill="none" stroke="var(--teal)" stroke-width="1.5"/>
      <defs>
        <linearGradient id="teamGrad" x1="0" y1="0" x2="1" y2="1">
          <stop offset="0" stop-color="#a9b7c3"/>
          <stop offset=".6" stop-color="#4d5d6c"/>
          <stop offset="1" stop-color="#2b3640"/>
        </linearGradient>
      </defs>
      <circle cx="405" cy="120" r="98" fill="url(#teamGrad)" role="img" aria-label="Photo of a team working together at a computer"/>
    </svg>
    <div class="band-label" style="left:42px;top:60px">VEXO.TRIM<small>HEALTH MONITORING SOLUTIONS</small></div>
    <div class="abs copy" style="left:40px;top:240px;width:440px">
      <h2 class="heading heading--md" style="margin-bottom:6px">PRODUCTS</h2>
      <p>The nature of Lintaro products is enterprise, strongly oriented to the cloud with proven robustness, performance and scalability.</p>
      <p>All products can be used via the web, even on the move via smartphones and tablets.</p>
      <p>Numerous software projects completed have allowed Lintaro to create packages that can be defined "for immediate use". Below are some of our achievements.</p>
    </div>
    <div class="columns copy" style="top:345px">
      <div class="col">
        <h3 class="heading heading--sm">CRM.TRIM</h3>
        <p>CRM.TRIM is a complete tool for managing customer relations, sales and contacts, with reports for every team.</p>
        <h3 class="heading heading--sm">EXPO.TRIM</h3>
        <p>EXPO.TRIM manages exhibitions and fairs, from stand booking to visitor access, and was used for large public events.</p>
        <p>The system handles several thousand users at once and keeps all data safe and always available.</p>
      </div>
      <div class="divider"></div>
      <div class="col">
        <h3 class="heading heading--sm">CLOUD.TRIM</h3>
        <p>CLOUD.TRIM is the base on which all Lintaro products run, offering secure hosting, backups and simple scaling for growing needs.</p>
        <h3 class="heading heading--sm">THING.TRIM</h3>
        <p>THING.TRIM connects sensors and devices, collecting their data in real time to monitor places and machines.</p>
        <p>It is used to control access, energy use and the state of remote plants.</p>
      </div>
    </div>
    <div class="brand brand--small" style="left:40px;top:655px"><span class="brand__dot"></span>lintaro</div>
    <div class="footer-rule" style="left:150px;top:676px;width:220px"></div>
    <div class="url-tab"><span class="url-tab__label">www.lintaro.it</span><span class="url-tab__num">02</span></div>
  </article>
</section>

<!-- ===== Solutions & technology spread ===== -->
<section class="spread spread--solutions">
  <article class="page">
    <svg class="abs" width="520" height="735" viewBox="0 0 520 735">
      <rect x="0" y="400" width="520" height="200" fill="var(--paper-2)"/>
      <path d="M0 0 L520 0 L520 170 C380 200 320 300 330 400 L0 400 Z" fill="var(--teal)"/>
      <circle cx="450" cy="330" r="138" fill="#fff"/>
      <circle cx="450" cy="330" r="130" fill="none" stroke="var(--teal)" stroke-width="1.5"/>
      <defs>
        <linearGradient id="careGrad" x1="0" y1="0" x2="1" y2="1">
          <stop offset="0" stop-color="#e6d8c9"/>
          <stop offset=".5" stop-color="#b99a80"/>
          <stop offset="1" stop-color="#8fa7b8"/>
        </linearGradient>
      </defs>
      <circle cx="450" cy="330" r="122" fill="url(#careGrad)" role="img" aria-label="Photo of an elderly couple wearing face masks"/>
    </svg>
    <div class="band-label" style="left:40px;top:30px">VEXO.TRIM<small>HEALTH MONITORING SOLUTIONS</small></div>
    <div class="abs copy copy--white" style="left:40px;top:85px;width:270px">
      <h3 class="heading heading--sm">HEALTH.TRIM</h3>
      <p>HEALTH.TRIM follows patients at home, collecting vital signs and alerting care staff when values change.</p>
      <h3 class="heading heading--sm">CARE.TRIM</h3>
      <p>CARE.TRIM organises the work of nurses and carers, with plans, visits and reports in one place.</p>
      <h3 class="heading heading--sm">BIZ.TRIM</h3>
      <p>BIZ.TRIM gives managers a clear view of costs, staff and results through simple dashboards.</p>
    </div>
    <div class="abs" style="left:40px;top:420px;width:290px">
      <ul class="bullets">
        <li><b>Orders:</b> creation and tracking of every request from start to end.</li>
        <li><b>IoT:</b> data from connected devices shown in real time.</li>
        <li><b>Forms:</b> digital forms that replace paper and speed up work.</li>
        <li><b>Reports:</b> clear summaries ready to share and print.</li>
      </ul>
    </div>
    <div class="label-tab" style="left:205px;top:548px">DOC.TRIM</div>
    <div class="abs copy" style="left:40px;top:585px;width:440px">
      <p>DOC.TRIM stores and shares documents safely, with versions, signatures and access rules for each user.</p>
    </div>
    <div class="brand brand--small" style="left:40px;top:655px"><span class="brand__dot"></span>lintaro</div>
    <div class="footer-rule" style="left:150px;top:676px;width:220px"></div>
    <div class="url-tab"><span class="url-tab__label">www.lintaro.it</span><span class="url-tab__num">03</span></div>
  </article>

  <article class="page">
    <svg class="abs" width="520" height="735" viewBox="0 0 520 735">
      <path d="M0 610 L520 600 L520 735 L0 735 Z" fill="var(--teal)"/>
    </svg>
    <div class="abs copy" style="left:40px;top:40px;width:440px">
      <p>Thus, the system allows you to insert, manage, update and create documents, including exchanges with other parties, and send them securely.</p>
      <p><b>The system was used among others for the management of all the practices of a large public event</b>, handling thousands of files for many participants.</p>
      <h3 class="heading heading--sm" style="font-size:13px">MAPS.TRIM</h3>
      <p>MAPS.TRIM shows places, routes and assets on interactive maps, linking each point to live data from the field.</p>
      <p>The system also allows you to display, move and manage objects on a map in a simple way.</p>
      <h4 class="heading" style="font-size:8px;margin:6px 0 4px">SOME OF THE EXAMPLES OF USE:</h4>
      <ul class="bullets">
        <li>Management of exhibition facilities at fairs.</li>
        <li>Waste route management integrated with artificial intelligence.</li>
        <li>Management of the maps of a large event site.</li>
        <li>Positioning and movement of devices in the field.</li>
      </ul>
    </div>
    <div class="tech-box copy">
      <h3 class="heading heading--md">TECHNOLOGY - KNOWLEDGE MANAGEMENT</h3>
      <p style="margin-top:6px">Lintaro keeps its skills up to date, using the main tools and languages of modern software and the cloud.</p>
      <div class="tech-grid">
        <span style="background:#f0d43a"></span><span style="background:#2f74c0"></span><span style="background:#6c3fa0"></span><span style="background:#5b2d8e"></span><span style="background:#1e88e5"></span><span style="background:#b0b6bb"></span><span style="background:#e44d26"></span><span style="background:#f29111"></span><span style="background:#333"></span><span style="background:#0a8ad6"></span>
        <span style="background:#3aa757"></span><span style="background:#222"></span><span style="background:#e34f26"></span><span style="background:#1572b6"></span><span style="background:#dd0031"></span><span style="background:#336791"></span><span style="background:#f7a41d"></span><span style="background:#0db7ed"></span><span style="background:#dc382d"></span><span style="background:#326ce5"></span>
        <span style="background:#0052cc"></span><span style="background:#68217a"></span><span style="background:#47a248"></span><span style="background:#f05032"></span><span style="background:#ff6f00"></span><span style="background:#00758f"></span><span style="background:#e10098"></span><span style="background:#4479a1"></span><span style="background:#1d63ed"></span><span style="background:#3c873a"></span>
      </div>
    </div>
    <div class="brand brand--light brand--small" style="left:40px;top:655px"><span class="brand__dot"></span>lintaro</div>
    <div class="url-tab"><span class="url-tab__label" style="background:#fff;color:var(--teal)">www.lintaro.it</span><span class="url-tab__num">04</span></div>
  </article>
</section>

</body>
</html>
```